Popular medical podcast needs artwork for special documentary series on the pandemic.

I have an established medical podcast called Quiet Harbour Rounds.

It's an "industry" podcast directed to doctors, nurses and other staff working in Intensive Care Units with the goal of helping to humanise our specialty.

The primary focus is to inspire the listeners to bring their best selves to work through conversations about compassion, communication, teamwork, patient bedside leadership and staff wellbeing.

So far there have been 69 episodes over 4 years. These have all been interviews with people I see as experts in these areas.

I am looking for artwork for a series of 7 episodes being produced as a documentary mini-series for the Quiet Harbour Rounds podcast.

This new series is a 6 part series (with a 7th "trailer" episode) and is an audio documentary focusing on the wellbeing of ICU staff who worked in busy ICUs in the USA and the UK during the COVID-19 pandemic.

The voices in each episode tell stories of their emotions, their struggles, the positives, how they coped (individually and as teams), how they looked after themselves, how they were supported, what helped, other learnings, and important take-aways. I narrate over the top to tell the guest's stories in a way that listeners can process what they've been through themselves, and so we can all take what's happened in the pandemic and learn from it.

Previous episodes of the podcast, before the series, had a photo of the guest as the podcast artwork (thumbprint).

Because this series has multiple guests and voices in each episode, I am therefore looking for an image that captures all of these things:

1. the COVID-19 pandemic
2. an ICU practitioner (doctor/nurse)
3. the series title "Lanterns Along The Long Night"
4. perhaps a smaller image of the regular podcast logo (I'm uploading this)
5. a place for editable text where the specific name of that episode is included.

So far these will be:
Episode 1 - "Trailer"
Episode 2 - "Done With Winter"
Episode 3 - "The kettle kept boiling"
Episode 4 - "Salt & silver days"
Episode 5 - (still working on a name)
Episode 6 - (still working on a name)

Basically I am after a single image to be used in all 7 episodes but with editable text for the 7 different episode titles.

I was thinking the image might include PPE (personal protective equipment) - like a mask or a face shield or both - or some other way of denoting the pandemic.

Perhaps the colouring and font might match the regular podcast logo but this is not a must.

```html
<!DOCTYPE html>
<html lang="en">
<head>
<meta charset="utf-8">
<title>Lanterns Along The Long Night – Series Artwork Variants</title>
<link rel="stylesheet" href="https://fonts.googleapis.com/css2?family=Montserrat:wght@500;700;800&family=Noticia+Text&display=swap">
<style>
  :root {
    --stage: #2e2e2e;
    --navy: #2e3192;
    --navy-glow: #3a40a0;
    --ink: #0a0a0a;
    --white: #ffffff;
    --lime: #8dc63f;
    --citron: #d9e021;
  }
  * { box-sizing: border-box; margin: 0; padding: 0; }
  html, body {
    width: 1200px; height: 1200px; overflow: hidden;
    background: var(--stage);
  }
  .stage { position: relative; width: 1200px; height: 1200px; }

  .cover {
    --accent: var(--lime);
    position: absolute;
    left: 334px;
    width: 534px; height: 533px;
    background: var(--navy);
    overflow: hidden;
    box-shadow: 0 8px 18px rgba(0,0,0,0.45);
  }
  .cover--lime { top: 46px; --accent: var(--lime); }
  .cover--citron { top: 627px; left: 333px; --accent: var(--citron); }

  .cover__artwork {
    position: absolute; left: 0; top: 234px; width: 534px; height: 299px;
    background:
      radial-gradient(ellipse 170px 230px at 390px 100px, rgba(90,100,190,0.35), transparent 70%),
      radial-gradient(circle 70px at 45px 160px, rgba(90,100,190,0.35), transparent 75%),
      radial-gradient(circle 40px at 185px 220px, rgba(90,100,190,0.25), transparent 75%);
  }

  .cover__band {
    position: absolute; left: 0; top: 0; width: 534px; height: 234px;
    background: var(--accent);
  }

  .cover__series {
    position: absolute; left: 46px; top: 0;
    font-family: "Noticia Text", Georgia, serif;
    font-size: 84px; line-height: 1; color: var(--ink);
    letter-spacing: 0.5px;
  }
  .cover__series span { position: absolute; left: 0; white-space: nowrap; }
  .cover__series .line-1 { top: 34px; }
  .cover__series .line-2 { top: 132px; }

  .cover__series-strong {
    position: absolute; left: 44px; top: 240px;
    font-family: "Montserrat", Arial, sans-serif;
    font-weight: 700; font-size: 66px; line-height: 1;
    color: var(--white); white-space: nowrap;
  }

  .cover__rule {
    position: absolute; left: 42px; top: 342px; width: 450px; height: 3px;
    background: var(--accent);
  }

  .cover__episode {
    position: absolute; left: 150px; top: 345px; width: 232px; height: 53px;
    background: var(--accent);
    display: flex; align-items: center; justify-content: center;
    font-family: "Montserrat", Arial, sans-serif;
    font-weight: 500; font-size: 26px; color: var(--white);
  }

  .cover__title {
    position: absolute; left: 0; top: 438px; width: 534px;
    text-align: center;
    font-family: "Noticia Text", Georgia, serif;
    font-size: 38px; letter-spacing: 4px; color: var(--white);
  }
</style>
</head>
<body>
<main class="stage">
  <section class="cover cover--lime">
    <div class="cover__artwork" role="img" aria-label="Faint illustration of a protective face mask and coronavirus particles"></div>
    <div class="cover__band"></div>
    <h1 class="cover__series">
      <span class="line-1">Lanterns</span>
      <span class="line-2">Along The</span>
    </h1>
    <div class="cover__series-strong">Long Night</div>
    <div class="cover__rule"></div>
    <div class="cover__episode">Episode 1</div>
    <div class="cover__title">TITLE GOES HERE</div>
  </section>

  <section class="cover cover--citron">
    <div class="cover__artwork" role="img" aria-label="Faint illustration of a protective face mask and coronavirus particles"></div>
    <div class="cover__band"></div>
    <h2 class="cover__series">
      <span class="line-1">Lanterns</span>
      <span class="line-2">Along The</span>
    </h2>
    <div class="cover__series-strong">Long Night</div>
    <div class="cover__rule"></div>
    <div class="cover__episode">Episode 1</div>
    <div class="cover__title">TITLE GOES HERE</div>
  </section>
</main>
</body>
</html>
```